THE MARKETPLACE FOR WAREHOUSE, the new way of doing logistics

We need an avant-garde, modern, minimalist and elegant web design for our company called VORDEN. This company represents the future of logistics, where users can find multiple offers of spaces (warehouse) in one place and other users can offer their available spaces to generate an extra cash inflow. A sample of this company is www.plindo-example.com, a US company that has developed this business. The closest thing to this type of business is NESTLOO, since it develops a similar model for people who offer spaces in their homes and people who need a space for a limited time. My domain site is www.vorden-example.com, where is the logo of my company. spanish- ------------------------------------------------ ---------------------------------------------- We need a web design avant-garde, modern, minimalist and elegant for our company called VORDEN. This company represents the future of logistics, where users can find multiple offers of spaces (wineries) in one place and other users can offer their available spaces to generate an extra profit. A sample of this company is www.plindo-example.com, a US company that has developed this business. The closest thing to this type of business is NESTLOO, since it develops a similar model for people who offer spaces in their homes and people who need a space for a limited time. My domain site is www.vorden-example.com, where is the logo of my company.

Target Market(s)

Companies, entrepreneurs, Companies, entrepreneurs,

Industry/Entity Type

Logistic

Number of Pages Required

5+ page

Colors
0d5aa6
ffffff
000000

Requirements
Must have
• A sober and minimalist homepage type quorbit, NstLoo. That is intuitive, must have spaces for advertising banners. You must always highlight the company logo. A sober and minimalist homepage like quorbit, NstLoo. That is intuitive, must have spaces for advertising banners. Must always highlight the company logo.

```html
<!DOCTYPE html>
<html lang="en">
<head>
<meta charset="utf-8">
<title>VORDEN – On-Demand Warehousing</title>
<link href="https://fonts.googleapis.com/css2?family=Open+Sans:ital,wght@0,400;0,600;0,700;1,400;1,600&family=Lato:wght@700&display=swap" rel="stylesheet">
<style>
:root{
  --brand:#0d5aa6;
  --brand-bright:#1d8fd3;
  --accent:#1e88c9;
  --ink:#1a1a1a;
  --muted:#444;
  --band:#5d6068;
  --press:#9a9a9a;
  --footer:#1d8fd3;
  --footer-deep:#0d3a5c;
  --white:#ffffff;
}
*{box-sizing:border-box;margin:0;padding:0}
html,body{width:742px;height:1200px;overflow:hidden;background:var(--white)}
body{font-family:"Open Sans",Arial,sans-serif;color:var(--ink);position:relative}

.hero{position:absolute;left:0;top:0;width:742px;height:396px;
  background:radial-gradient(ellipse at 50% 75%,#8a8170 0%,#4a4540 35%,#2a2725 75%,#1c1a19 100%);}
.hero-brand{position:absolute;top:70px;left:0;width:742px;text-align:center}
.hero-brand .mark{display:inline-flex;align-items:center;gap:10px}
.hero-brand .dot{width:40px;height:40px;border-radius:50%;background:var(--accent)}
.hero-brand .name{font-size:32px;font-weight:700;color:var(--accent);letter-spacing:3px;line-height:1}
.hero-brand .tag{display:block;font-size:8.5px;letter-spacing:2.4px;color:var(--white);font-weight:600;margin:4px 0 0 56px}
.hero h1{position:absolute;top:176px;width:742px;text-align:center;color:var(--white);font-size:27px;font-weight:700;letter-spacing:1.5px}
.hero .lead{position:absolute;top:211px;width:742px;text-align:center;color:#eee;font-size:9.5px}
.search{position:absolute;top:244px;left:190px;display:flex;gap:9px}
.search .field{width:274px;height:24px;background:var(--white);font-size:8px;color:#333;padding:7px 6px}
.search .btn{width:78px;height:24px;background:var(--brand-bright);color:var(--white);font-size:9px;font-weight:600;text-align:center;line-height:24px}

.features{position:absolute;top:396px;left:0;width:742px;height:153px}
.feature{position:absolute;top:26px;width:200px;text-align:center}
.feature svg{display:block;margin:0 auto 6px}
.feature h3{font-size:14.5px;font-weight:600;color:var(--ink)}
.feature p{font-size:10.5px;line-height:14px;color:var(--muted);margin-top:3px}

.quotes{position:absolute;top:549px;left:0;width:742px;height:173px;background:var(--band)}
.quote{position:absolute;top:37px;width:330px;text-align:center;color:var(--white);font-family:"Lato","Open Sans",sans-serif;font-weight:700;font-size:10.5px;line-height:17px}
.quote cite{display:block;font-family:"Open Sans",sans-serif;font-style:italic;font-weight:400;font-size:8.5px;margin-top:14px}
.dots{position:absolute;top:146px;left:359px;display:flex;gap:10px}
.dots span{width:6px;height:6px;border-radius:50%;background:#8a8d94}
.dots span.on{background:#d0d2d6}

.press{position:absolute;top:735px;left:0;width:742px;display:flex;justify-content:center;align-items:center;gap:40px;color:var(--press)}
.press span{font-size:13px;font-weight:600}
.press .badge{width:36px;height:32px;background:#c8c8c8}

.listings{position:absolute;top:798px;left:47px;width:650px}
.listings h2{font-size:16.5px;font-weight:600;color:var(--accent)}
.cards{display:flex;gap:12px;margin-top:12px}
.card{width:153px}
.card .photo{height:104px}
.card h4{font-size:10.5px;font-weight:600;margin-top:9px}
.rates{display:flex;justify-content:space-between;margin-top:4px;font-size:7.5px;color:#333;line-height:11px}
.rates b{font-weight:700}
.show-all{display:block;margin-top:28px;font-size:11.5px;color:var(--accent)}

.footer{position:absolute;top:1040px;left:0;width:742px;height:136px;background:var(--footer);color:var(--white)}
.foot-brand{position:absolute;left:60px;top:9px}
.foot-brand .mark{display:flex;align-items:center;gap:6px}
.foot-brand .dot{width:24px;height:24px;border-radius:50%;border:2px solid var(--white)}
.foot-brand .name{font-size:18px;font-weight:700;letter-spacing:2px}
.foot-brand .tag{font-size:5px;letter-spacing:1.4px;margin-left:30px;display:block}
.contact{position:absolute;left:61px;top:50px;font-size:7.5px;line-height:15.3px}
.contact b{font-weight:700}
.col{position:absolute;top:12px}
.col h5{font-size:10px;font-weight:600;margin-bottom:7px}
.col ul{list-style:none}
.col li{font-size:8px;line-height:16.8px;padding-left:10px;position:relative}
.col.arrows li::before{content:"";position:absolute;left:1px;top:6px;border-left:4px solid var(--white);border-top:3px solid transparent;border-bottom:3px solid transparent}
.legal{position:absolute;left:0;top:1176px;width:742px;height:24px;background:var(--footer-deep);color:var(--white);font-size:8.5px;font-style:italic;padding:6px 60px}
</style>
</head>
<body>

<header class="hero" role="img" aria-label="Photo of a tall warehouse aisle with shelves of cardboard boxes">
  <div class="hero-brand">
    <div class="mark"><span class="dot"></span><span class="name">VORDEN</span></div>
    <span class="tag">ON-DEMAND WAREHOUSING</span>
  </div>
  <h1>FIND WAREHOUSE</h1>
  <p class="lead">Discover many available spaces perfect for your needs</p>
  <div class="search">
    <div class="field">City, State or ZIP...</div>
    <div class="btn">Search</div>
  </div>
</header>

<section class="features">
  <div class="feature" style="left:54px">
    <svg width="42" height="36" viewBox="0 0 42 36"><path d="M2 12 L21 2 L40 12 V34 H2Z" fill="var(--accent)"/><rect x="9" y="15" width="24" height="19" fill="#fff"/><rect x="11" y="24" width="6" height="8" fill="var(--accent)"/><rect x="18" y="24" width="6" height="8" fill="var(--accent)"/><rect x="25" y="24" width="6" height="8" fill="var(--accent)"/><rect x="11" y="17" width="20" height="2" fill="var(--accent)"/></svg>
    <h3>Inventory Overflow</h3>
    <p>Add storage capacity instantly to<br>fulfill your needs</p>
  </div>
  <div class="feature" style="left:270px">
    <svg width="42" height="36" viewBox="0 0 42 36"><path d="M2 34 L9 22 H33 L40 34Z" fill="none" stroke="var(--accent)" stroke-width="2"/><path d="M21 30 C13 20 12 16 12 12 A9 9 0 0 1 30 12 C30 16 29 20 21 30Z" fill="#fff" stroke="var(--accent)" stroke-width="2.2"/><circle cx="21" cy="12" r="3.5" fill="none" stroke="var(--accent)" stroke-width="2"/></svg>
    <h3>Nearby Storage</h3>
    <p>Find available warehaouse<br>near you</p>
  </div>
  <div class="feature" style="left:486px">
    <svg width="46" height="36" viewBox="0 0 46 36"><rect x="14" y="2" width="16" height="15" rx="2" fill="var(--accent)"/><path d="M22 5 L26 9 H23.5 V13 H20.5 V9 H18Z" fill="#fff"/><path d="M2 24 C8 20 14 20 20 23 H28 C30 23 30 26 28 26 H19 M2 32 C10 30 18 34 26 31 L38 24 C40 22 38 20 36 21 L28 25" fill="none" stroke="var(--accent)" stroke-width="2.2"/><rect x="38" y="17" width="6" height="17" fill="var(--accent)"/></svg>
    <h3>Maximize your utilization</h3>
    <p>Generate cash from your<br>underutilized assets.</p>
  </div>
</section>

<section class="quotes">
  <blockquote class="quote" style="left:22px">I contacted VORDEN to find the right space and service partner and very quickly we were good to go and able to start moving product immediately.<cite>—Brinkley Hardware</cite></blockquote>
  <blockquote class="quote" style="left:393px">VORDEN made it possible to expand our pop-up stores into three new markets without exceeding our budget. Looking down the line, we see a lot of different ways VORDEN can help save us money and add flexibility to our warehouse strategy.<cite>—LUMA</cite></blockquote>
  <div class="dots"><span class="on"></span><span></span></div>
</section>

<section class="press">
  <span>The Market Ledger</span>
  <span>Meridian</span>
  <span>Stockwell</span>
  <span>Kestrel News</span>
  <span class="badge"></span>
</section>

<section class="listings">
  <h2>Available Warehouse</h2>
  <div class="cards">
    <article class="card">
      <div class="photo" role="img" aria-label="Indoor self-storage corridor with blue doors" style="background:linear-gradient(90deg,#1f3f9a,#6d8fd8 50%,#d6dbe6)"></div>
      <h4>Bentonville, AR</h4>
      <div class="rates"><span>Lowest Labor Cost<br><b>$7.80</b> per Pallet</span><span>Lowest Storage Cost<br><b>$6.50</b> per Pallet</span></div>
    </article>
    <article class="card">
      <div class="photo" role="img" aria-label="Rows of outdoor storage units with green doors under a cloudy sky" style="background:linear-gradient(180deg,#c9d6e2 0%,#e9eef2 35%,#5f7a5e 55%,#7b7775 100%)"></div>
      <h4>Mobile, AL</h4>
      <div class="rates"><span>Lowest Labor Cost<br><b>$6.80</b> per Pallet</span><span>Lowest Storage Cost<br><b>$5.50</b> per Pallet</span></div>
    </article>
    <article class="card">
      <div class="photo" role="img" aria-label="Truck parked inside a large blue-lit warehouse hall" style="background:linear-gradient(180deg,#2f6fb0,#5f96c8 55%,#3a5f88)"></div>
      <h4>Madison, AL</h4>
      <div class="rates"><span>Lowest Labor Cost<br><b>$6.80</b> per Pallet</span><span>Lowest Storage Cost<br><b>$5.50</b> per Pallet</span></div>
    </article>
    <article class="card">
      <div class="photo" role="img" aria-label="Modern warehouse building with a truck under a blue sky" style="background:linear-gradient(180deg,#2b7fd0 0%,#6fb1e8 50%,#9a9a98 75%,#b9b7b2 100%)"></div>
      <h4>Phoenix, AZ</h4>
      <div class="rates"><span>Lowest Labor Cost<br><b>$7.90</b> per Pallet</span><span>Lowest Storage Cost<br><b>$5.69</b> per Pallet</span></div>
    </article>
  </div>
  <a class="show-all">Show All (50,000+) &gt;</a>
</section>

<footer class="footer">
  <div class="foot-brand">
    <div class="mark"><span class="dot"></span><span class="name">VORDEN</span></div>
    <span class="tag">ON-DEMAND WAREHOUSING</span>
  </div>
  <div class="contact">
    VORDEN Co.<br>
    <b>24 Hours Service:</b> 555-014-2778<br>
    <b>Email:</b> info@vorden-example.org<br>
    <b>Address:</b> Calle Los Olmos 12-40 y Alameda, Quito<br>
    <b>Tel/Fax:</b> 555-014-2779
  </div>
  <nav class="col arrows" style="left:300px">
    <h5>Discover</h5>
    <ul><li>About Warehouse</li><li>Tips to rent</li><li>10 Reasons for choosing Vorden</li><li>Experiences</li><li>Guidance</li><li>Connectivity</li></ul>
  </nav>
  <nav class="col arrows" style="left:464px">
    <h5>Hosting</h5>
    <ul><li>Why host</li><li>Maximize your utilization</li><li>Responsible</li><li>Term &amp; Conditions</li></ul>
  </nav>
  <nav class="col" style="left:614px;top:35px">
    <ul><li>Terms</li><li>Privacy</li><li>Site Map</li></ul>
  </nav>
</footer>
<div class="legal">All contents ©2018 VORDEN. &nbsp; All rights reserved.</div>

</body>
</html>
```